Engineering group involved with fire safety needs a business card

We need a business card design for a company based in Greece called "Varotis Group". We are engineers and specialized technicians, operating the following : a) Fire fighting equipment trade b) Installation , Inspection & Maintenance of fire extinguishers and fire protection systems c) Occupational Health & Safety (Risk assessment & management/ Staff training). We need a clear and simple card design. I uploaded a draft I made, in order to give you an idea of the company and how I currently imagine the design of the card. I also uploaded the logo in .png file format. We are always open to different, new suggestions and ideas you may want to submit.
Target Market(s)
industries, companies, managers, retail clients
Industry/Entity Type
Fire Safety
Contact Information for Business Card
Addresses & phone numbers (headquarters + branch), logo, name (you can find all the details on the uploaded files!)
Colors
Designer to choose colors to be used in the design.
Look and feel
Each slider illustrates characteristics of the customer's brand and the style your logo design should communicate.

```html
<!DOCTYPE html>
<html lang="en">
<head>
<meta charset="utf-8">
<title>Varotis Group – Business Card</title>
<link rel="stylesheet" href="https://fonts.googleapis.com/css2?family=Montserrat:wght@300;400;500;600&family=Oswald:wght@500&family=PT+Sans&display=swap">
<style>
  :root {
    --page-bg: #ecedef;
    --card-light: #ffffff;
    --card-dark: #3f4648;
    --brand-red: #a6121f;
    --ink: #333638;
    --ink-soft: #3f4446;
    --on-dark: #ffffff;
  }
  * { margin: 0; padding: 0; box-sizing: border-box; }
  html, body { width: 1200px; height: 1200px; overflow: hidden; }
  body { background: var(--page-bg); position: relative; }

  .card {
    position: absolute;
    top: 150px;
    width: 532px;
    height: 869px;
    overflow: hidden;
  }
  .card--front { left: 42px; background: var(--card-light); border: 1px solid #2a2a2a; }
  .card--back { left: 619px; background: var(--card-dark); }

  .card__line { position: absolute; left: 0; width: 100%; white-space: nowrap; }
  .centered { text-align: center; }

  .brand {
    top: 155px;
    display: flex;
    justify-content: center;
    align-items: center;
    gap: 14px;
    font-family: "Montserrat", sans-serif;
    font-weight: 600;
    font-size: 44px;
    letter-spacing: 1px;
    text-transform: uppercase;
  }
  .brand__square { width: 28px; height: 28px; display: block; }
  .card--front .brand { color: var(--brand-red); }
  .card--front .brand__square { background: var(--brand-red); }
  .card--back .brand { color: var(--on-dark); }
  .card--back .brand__square { background: var(--on-dark); }

  .tagline {
    top: 272px;
    font-family: "Oswald", sans-serif;
    font-weight: 500;
    font-size: 27px;
    letter-spacing: 0.2px;
    transform: scaleX(0.92);
  }
  .card--front .tagline { color: var(--brand-red); }
  .card--back .tagline { color: var(--on-dark); }

  .person__name {
    top: 342px;
    font-family: "Montserrat", sans-serif;
    font-weight: 500;
    font-size: 31px;
    letter-spacing: 1.5px;
    color: var(--ink);
  }
  .person__role {
    font-family: "PT Sans", sans-serif;
    font-size: 26px;
    line-height: 34px;
    color: var(--ink-soft);
  }
  .person__role--1 { top: 394px; }
  .person__role--2 { top: 428px; }

  .accent-bar {
    position: absolute;
    left: 0;
    width: 18px;
    background: var(--brand-red);
  }
  .card--front .accent-bar { top: 504px; height: 89px; }
  .card--back .accent-bar { top: 469px; height: 142px; }

  .contact {
    position: absolute;
    left: 39px;
    font-family: "PT Sans", sans-serif;
    color: var(--ink-soft);
  }
  .contact--phones { top: 498px; font-size: 27px; line-height: 34.5px; }
  .contact--email { top: 620px; font-size: 27px; }
  .contact--address { top: 670px; font-size: 23px; line-height: 30px; }

  .website--front {
    top: 814px;
    font-family: "Montserrat", sans-serif;
    font-size: 29px;
    color: var(--brand-red);
    letter-spacing: 0.5px;
  }

  .services {
    position: absolute;
    left: 38px;
    top: 464px;
    list-style: none;
    font-family: "Montserrat", sans-serif;
    font-weight: 500;
    font-size: 19px;
    letter-spacing: 1px;
    line-height: 42.3px;
    color: var(--on-dark);
    text-transform: uppercase;
  }

  .online {
    font-family: "Montserrat", sans-serif;
    font-weight: 400;
    font-size: 31px;
    letter-spacing: 0.8px;
    color: var(--on-dark);
  }
  .online--email { top: 764px; }
  .online--web { top: 806px; }
</style>
</head>
<body>

  <section class="card card--front" aria-label="Business card front">
    <div class="card__line brand"><span class="brand__square"></span>Varotis Group</div>
    <div class="card__line centered tagline">INSTALLATION - INSPECTION - MAINTENANCE</div>

    <div class="card__line centered person__name">STAVROS VAROTIS</div>
    <div class="card__line centered person__role person__role--1">Mechanical Engineer</div>
    <div class="card__line centered person__role person__role--2">OHS Consultant</div>

    <span class="accent-bar"></span>
    <div class="contact contact--phones">
      Tel. (HQ) +30 22920 10482<br>
      Tel. (BO) +30 210 5547120<br>
      Mob. +30 694 120 33 58
    </div>
    <div class="contact contact--email">stavros.varotis@varotisgroup.gr</div>
    <div class="contact contact--address">
      Headquarters:<br>
      12 Agiou Nikolaou, 19500 Lavrio<br>
      Branch Office:<br>
      45 Thessalonikis, 15124 Marousi
    </div>

    <div class="card__line centered website--front">www.varotisgroup.gr</div>
  </section>

  <section class="card card--back" aria-label="Business card back">
    <div class="card__line brand"><span class="brand__square"></span>Varotis Group</div>
    <div class="card__line centered tagline">INSTALLATION - INSPECTION - MAINTENANCE</div>

    <span class="accent-bar"></span>
    <ul class="services">
      <li>Fire Fighting Equipment</li>
      <li>Licencing &amp; Business Registration</li>
      <li>Occupational Health &amp; Safety</li>
      <li>Staff Training</li>
    </ul>

    <div class="card__line centered online online--email">info@varotisgroup.gr</div>
    <div class="card__line centered online online--web">www.varotisgroup.gr</div>
  </section>

</body>
</html>
```